ORVET - Helping People with Disabilities

ORVET is a nonprofit that strives to enable people with physical disabilities to live meaningful, quality lives. ORVET needs a professional attractive website that:
• establishes a strong brand image
• presents Orvet's services to those who need it
• raises funds from potential donors
Please see WORD DOC attached for more information about design vision.

Target Market(s)

people with disabilities

Industry/Entity Type

charity website

Number of Pages Required

2 page

Font styles to use
Sans Serif

Requirements
Must have
• 1. 2 pages means 1 design for homepage and 1 design for top of inner pages (banner ideas)
Nice to have
• please see attached design brief (WORD DOC)

```html
<!DOCTYPE html>
<html lang="en">
<head>
<meta charset="utf-8">
<title>ORVET – A Good Life For Everyone</title>
<link href="https://fonts.googleapis.com/css2?family=Ubuntu:wght@400;500;700&display=swap" rel="stylesheet">
<style>
:root{
  --green:#3bb54a;
  --teal-dark:#0c6e68;
  --teal:#23b7b0;
  --teal-pale:#e7f6f5;
  --ink:#111;
  --grey:#6d6d6d;
  --panel:#eaf4fb;
}
*{margin:0;padding:0;box-sizing:border-box}
html,body{width:1200px;height:3823px;overflow:hidden}
body{font-family:'Ubuntu',sans-serif;color:var(--ink);background:#fff;position:relative}
.abs{position:absolute}
.btn{position:absolute;display:flex;align-items:center;color:#fff;font-weight:500}
.btn .face{height:100%;background:var(--green);display:flex;align-items:center;justify-content:center;clip-path:polygon(6% 0,100% 0,92% 100%,0 100%)}
.btn .tip{width:38px;height:100%;background:var(--green);clip-path:polygon(50% 0,100% 100%,0 100%);margin-left:-12px}
.section-title{position:absolute;font-weight:500;text-transform:uppercase;letter-spacing:.5px}
.rule{position:absolute;height:3px;background:var(--teal-dark)}

/* hero */
.hero{left:0;top:0;width:1200px;height:610px;background:linear-gradient(120deg,#cfe3ea 0%,#b8cbc0 35%,#c9a98e 60%,#9fb896 100%)}
.hero-curve{left:0;top:540px;width:1200px;height:120px}
.brand{left:98px;top:40px;display:flex;align-items:center;gap:10px;font-size:30px;font-weight:700;color:var(--teal-dark)}
.brand i{width:22px;height:22px;background:var(--green);display:block}
.nav{top:46px;font-size:17px;color:#222}
.hero-title{left:101px;top:176px;font-size:35px;font-weight:500;line-height:44px;color:#111}
.know{left:98px;top:389px;width:1002px;height:258px;background:var(--panel);border-radius:6px;display:flex;padding:18px 0}
.know .col{flex:1;text-align:center;border-right:1px solid #d5dde3;padding:4px 18px}
.know .col:last-child{border-right:none}
.know .ico{width:84px;height:84px;border-radius:50%;background:#dcdcdc;margin:0 auto 18px;display:flex;align-items:center;justify-content:center}
.know h3{font-size:21px;font-weight:500;margin-bottom:10px}
.know p{font-size:13px;color:var(--grey);line-height:22px}

/* about */
.about-text{left:98px;width:460px;font-size:15.5px;line-height:23px;color:#444}
.about-frame{left:623px;top:727px;width:472px;height:458px;background:linear-gradient(180deg,var(--green),var(--teal-dark));clip-path:polygon(0 0,100% 0,100% 100%,95% 95%,95% 5%,4% 5%)}
.about-photo{left:602px;top:750px;width:466px;height:453px;background:linear-gradient(160deg,#f3c35a,#c98d33 55%,#8f6a3a)}

/* offer */
.offer{left:0;top:1261px;width:1200px;height:606px;background:#000;color:#fff}
.offer-card{position:absolute;top:220px;width:244px}
.offer-card .pic{height:162px}
.offer-card h3{font-size:21px;font-weight:500;margin-top:22px;line-height:27px;text-transform:uppercase}
.offer-card p{position:absolute;top:263px;font-size:15.5px;line-height:21.5px;width:236px}

/* band */
.band{left:0;top:1866px;width:1200px;height:270px;background:linear-gradient(90deg,#0b6663,#0f7573 50%,#0b6663)}
.band h2{position:absolute;top:78px;width:100%;text-align:center;font-size:25px;font-weight:500;color:#fff}

/* news */
.news-item{position:absolute;left:93px;width:444px;height:140px;background:var(--teal-pale);padding:12px}
.news-item.active{background:var(--teal);color:#fff}
.news-item .pic{position:absolute;left:11px;top:12px;width:118px;height:116px;background:linear-gradient(135deg,#c7b6a4,#7b6a5b)}
.news-item h4{position:absolute;left:153px;top:30px;font-size:15.5px;font-weight:500}
.news-item p{position:absolute;left:153px;top:58px;width:275px;font-size:11px;line-height:16px;color:#666}
.news-item.active p{color:#eaffff}
.news-item a{position:absolute;left:157px;top:108px;font-size:14.5px;color:var(--teal-dark);font-weight:500;text-decoration:none}
.news-item.active a{color:#fff}
.map{left:593px;top:2400px;width:534px;height:330px;background:radial-gradient(ellipse at center,#d4d4d4 0%,#e2e2e2 55%,#fff 75%)}

/* contact */
.contact{left:0;top:2870px;width:1200px;height:660px;background:linear-gradient(180deg,#2ab8b2,#22aca6)}
.field{position:absolute;border:1.5px solid #e6fbfa;border-radius:4px;color:#fff;font-size:18px;padding:16px 18px}

/* footer */
.foot-title{position:absolute;top:3580px;font-size:25px;font-weight:500}
.foot-rule{position:absolute;top:3626px;width:74px;height:2px;background:var(--teal)}
.foot-text{font-size:15.5px;line-height:21px;color:#777}
.social{position:absolute;top:3650px;width:35px;height:35px;border-radius:50%;border:2px solid #556}
.detail{position:absolute;left:879px;font-size:15.5px;line-height:22px;color:#222}
</style>
</head>
<body>

<!-- hero -->
<div class="abs hero" role="img" aria-label="Photo of a smiling caregiver embracing an elderly woman outdoors"></div>
<svg class="abs hero-curve" viewBox="0 0 1200 120" preserveAspectRatio="none"><path d="M0 70 Q600 -20 1200 70 L1200 120 L0 120Z" fill="#fff"/></svg>
<div class="abs brand"><i></i>ORVET</div>
<div class="abs nav" style="left:273px">About</div>
<div class="abs nav" style="left:369px">Programs</div>
<div class="abs nav" style="left:491px">Rehabilitation And Sports</div>
<div class="abs nav" style="left:738px">Rights Realization</div>
<div class="abs nav" style="left:925px">News</div>
<div class="abs nav" style="left:1016px">Contact Us</div>
<h1 class="abs hero-title">A Good Life For Everyone<br>Like Everyone</h1>
<div class="btn" style="left:101px;top:292px;height:47px;font-size:16px"><span class="face" style="width:260px">Donate to help us help them</span><span class="tip"></span></div>

<div class="abs know">
  <div class="col"><div class="ico"><svg width="44" height="44" viewBox="0 0 44 44" fill="none" stroke="#333" stroke-width="2"><circle cx="22" cy="7" r="4"/><path d="M22 12v14h10l4 10"/><circle cx="18" cy="30" r="9"/></svg></div><h3>I Want to know</h3><p>What are all the rights available to people with physical disabilities and their families</p></div>
  <div class="col"><div class="ico"><svg width="44" height="44" viewBox="0 0 44 44" fill="none" stroke="#333" stroke-width="2"><rect x="18" y="4" width="22" height="16"/><path d="M22 9h14M22 14h10"/><circle cx="12" cy="18" r="3"/><circle cx="12" cy="34" r="7"/></svg></div><h3>I Want to know</h3><p>Where I can join online classes offered by ORVET</p></div>
  <div class="col"><div class="ico"><svg width="44" height="44" viewBox="0 0 44 44" fill="none" stroke="#333" stroke-width="2"><rect x="22" y="4" width="18" height="12" rx="2"/><circle cx="18" cy="24" r="7"/><path d="M6 42c2-8 22-8 24 0"/></svg></div><h3>I Want to know</h3><p>What services there are for children with disabilities</p></div>
  <div class="col"><div class="ico"><svg width="44" height="44" viewBox="0 0 44 44" fill="none" stroke="#333" stroke-width="2"><path d="M6 22 22 8l16 14"/><path d="M10 19v19h24V19"/><circle cx="22" cy="28" r="5"/><circle cx="35" cy="9" r="4"/></svg></div><h3>I Want to know</h3><p>If there is a rehabilitation center in my area</p></div>
</div>

<!-- about -->
<h2 class="section-title" style="left:98px;top:726px;font-size:38px">About Us</h2>
<p class="abs about-text" style="top:810px">Lorem ipsum dolor sit amet, consectetur adipiscing elit, sed do eiusmod tempor incididunt ut labore et dolore magna aliqua. Ut enim ad minim veniam, quis nostrud exercitation ullamco laboris nisi ut aliquip ex ea commodo consequat. Duis aute irure dolor in reprehenderit in voluptate velit esse cillum dolore eu fugiat nulla pariatur.</p>
<p class="abs about-text" style="top:970px">Lorem ipsum dolor sit amet, consectetur adipiscing elit, sed do eiusmod tempor incididunt ut labore et dolore magna aliqua. Ut enim ad minim veniam, quis nostrud exercitation ullamco laboris nisi ut aliquip ex ea commodo consequat. Duis aute irure dolor in reprehenderit in voluptate velit esse cillum dolore eu fugiat nulla pariatur.</p>
<div class="btn" style="left:98px;top:1157px;height:38px;font-size:15px"><span class="face" style="width:136px">Read More</span><span class="tip"></span></div>
<div class="abs about-frame"></div>
<div class="abs about-photo" role="img" aria-label="Photo of a laughing child in a wheelchair with his mother in golden sunlight"></div>

<!-- offer -->
<div class="abs offer">
  <svg class="abs" style="left:0;top:0" width="1200" height="90" viewBox="0 0 1200 90"><polygon points="0,0 1200,0 1200,2 600,70 0,2" fill="#fff"/><polygon points="0,2 600,70 1200,2 1200,12 600,84 0,12" fill="var(--teal-dark)"/></svg>
  <h2 class="section-title" style="left:98px;top:114px;font-size:38px">What We Offer You</h2>
  <div class="rule" style="left:98px;top:171px;width:77px"></div>
  <div class="offer-card" style="left:98px"><div class="pic" role="img" aria-label="Photo of a student with a laptop before a colourful mural" style="background:linear-gradient(135deg,#eee,#c9c9c9)"></div><h3>Education</h3><p>ORVET works to impart education and knowledge to people with disabilities and operates the dedicated campus</p></div>
  <div class="offer-card" style="left:351px"><div class="pic" role="img" aria-label="Photo of a trainer helping an older man lift dumbbells" style="background:linear-gradient(135deg,#dfe3e6,#8fa3b0)"></div><h3>Sports And Rehab</h3><p>ORVET encourages people with disabilities to play sports and find new strengths in themselves</p></div>
  <div class="offer-card" style="left:605px"><div class="pic" role="img" aria-label="Photo of a man on a bench watching a sunset over the water" style="background:linear-gradient(180deg,#d48a5e,#6f7c99 60%,#3b3b45)"></div><h3>Rights Realization</h3><p>ORVET promotes policies concerning people with physical-motor disabilities, promotes their rights,</p></div>
  <div class="offer-card" style="left:859px"><div class="pic" role="img" aria-label="Photo of volunteers packing donation boxes" style="background:linear-gradient(135deg,#b99a7c,#6b5a4c)"></div><h3>Community<br>Infrastructure</h3><p>INFRASTRUCTURE ORVET owns the association's houses all over the country,rehabilitation day centers</p></div>
</div>

<!-- band -->
<div class="abs band">
  <h2>Even people with disabilities can be with everyone, like everyone</h2>
  <div class="btn" style="left:454px;top:145px;height:50px;font-size:16px"><span class="face" style="width:262px">Don't leave them behind</span><span class="tip"></span></div>
</div>

<!-- news + map -->
<h2 class="section-title" style="left:98px;top:2228px;font-size:38px">News</h2>
<div class="rule" style="left:98px;top:2282px;width:77px"></div>
<h2 class="section-title" style="left:639px;top:2228px;font-size:38px">Map Of Branches</h2>
<div class="rule" style="left:639px;top:2282px;width:77px"></div>

<div class="news-item" style="top:2331px"><div class="pic" role="img" aria-label="Photo of a caregiver talking with a man in a wheelchair"></div><h4>Sed ut perspiciatis unde omnis</h4><p>Lorem ipsum dolor sit amet, consectetur adipiscing elit, sed do eiusmod tempor incididunt ut labore et dolore magna aliqua.</p><a>Read More</a></div>
<div class="news-item active" style="top:2487px"><div class="pic" role="img" aria-label="Photo of a volunteer visiting an elderly woman"></div><h4>Sed ut perspiciatis unde omnis</h4><p>Lorem ipsum dolor sit amet, consectetur adipiscing elit, sed do eiusmod tempor incididunt ut labore et dolore magna aliqua.</p><a>Read More</a></div>
<div class="news-item" style="top:2646px"><div class="pic" role="img" aria-label="Photo of friends gathered around a man in a wheelchair"></div><h4>Sed ut perspiciatis unde omnis</h4><p>Lorem ipsum dolor sit amet, consectetur adipiscing elit, sed do eiusmod tempor incididunt ut labore et dolore magna aliqua.</p><a>Read More</a></div>

<div class="abs map" role="img" aria-label="Grey world map with pins marking branch locations"></div>

<!-- contact -->
<div class="abs contact">
  <h2 class="section-title" style="left:0;width:1200px;text-align:center;top:42px;font-size:38px;color:#111">Contact Us</h2>
  <div class="rule" style="left:553px;top:96px;width:92px"></div>
  <div class="field" style="left:148px;top:152px;width:448px;height:56px">First Name</div>
  <div class="field" style="left:611px;top:152px;width:439px;height:56px">Last Name</div>
  <div class="field" style="left:148px;top:237px;width:448px;height:56px">Phone</div>
  <div class="field" style="left:611px;top:237px;width:439px;height:56px">Email</div>
  <div class="field" style="left:148px;top:311px;width:902px;height:152px">Messages</div>
  <div class="btn" style="left:512px;top:496px;height:50px;font-size:16px"><span class="face" style="width:152px">Send Now</span><span class="tip"></span></div>
  <svg class="abs" style="left:0;top:580px" width="1200" height="80" viewBox="0 0 1200 80"><polygon points="0,50 600,0 1200,50 1200,80 0,80" fill="var(--teal-dark)"/><polygon points="0,70 600,20 1200,70 1200,80 0,80" fill="#fff"/></svg>
</div>

<!-- footer -->
<h3 class="foot-title" style="left:99px">ABOUT US</h3>
<div class="foot-rule" style="left:99px"></div>
<p class="abs foot-text" style="left:97px;top:3646px;width:300px">Lorem ipsum dolor sit amet, consectetur adipiscing elit, sed do eiusmod tempor incididunt ut labore et dolore magna</p>
<div class="abs" style="left:96px;top:3754px;font-size:15.5px">brightpage.net</div>

<h3 class="foot-title" style="left:498px">SOCIAL MEDIA</h3>
<div class="foot-rule" style="left:498px"></div>
<div class="social" style="left:497px;border-color:#c2357f"></div>
<div class="social" style="left:539px;border-color:#3b5b9a"></div>
<div class="social" style="left:582px;border-color:#222"></div>
<div class="social" style="left:624px;border-color:#d22"></div>
<div class="social" style="left:666px;border-color:#1f6fb0"></div>
<div class="abs" style="left:0;width:1200px;text-align:center;top:3751px;font-size:19px">© 2023 ORVET . All Rights Reserved.</div>

<h3 class="foot-title" style="left:845px">CONTACT DETAILS</h3>
<div class="foot-rule" style="left:845px"></div>
<svg class="abs" style="left:846px;top:3645px" width="14" height="18" viewBox="0 0 14 18"><path d="M7 0a7 7 0 0 0-7 7c0 5 7 11 7 11s7-6 7-11a7 7 0 0 0-7-7z" fill="var(--teal-dark)"/><circle cx="7" cy="7" r="2.5" fill="#fff"/></svg>
<div class="detail" style="top:3645px">Lorem ipsum dolor sit amet,<br>consectetur adipiscing</div>
<svg class="abs" style="left:846px;top:3708px" width="16" height="16" viewBox="0 0 16 16"><path d="M3 1l3 3-2 2c1 2 3 4 6 6l2-2 3 3-2 2C7 15 1 9 1 3z" fill="var(--teal-dark)"/></svg>
<div class="detail" style="top:3705px">+1 888-888-8888</div>
<svg class="abs" style="left:846px;top:3756px" width="18" height="13" viewBox="0 0 18 13"><rect width="18" height="13" fill="var(--teal-dark)"/><path d="M0 0l9 7 9-7" stroke="#fff" stroke-width="1.5" fill="none"/></svg>
<div class="detail" style="top:3752px">info@orvet.org</div>

<div class="abs" style="left:1127px;top:3737px;width:45px;height:45px;background:var(--green);display:flex;align-items:center;justify-content:center"><svg width="18" height="18" viewBox="0 0 18 18"><path d="M9 2 2 10h4v6h6v-6h4z" fill="#fff"/></svg></div>

</body>
</html>
```